Business Card Design for Marketing Firm

Looking for business card design for higher end marketing firm. Clean but impressionable/trendy. We are a marketing firm that represents manufacturers in the foodservice equipment and supply industry. Our customers are end users such has hotels, restaurants, country clubs, convention centers and casinos as well as distributors of restaurants supplies and equipment, and manufacturers of foodservice equipment and supplies.
Target Market(s)
Hotels, Restaurants, Supply & Equipment Distributors, Foodservice Manufacturers
Industry/Entity Type
Foodservice/Hospitality
Contact Information for Business Card
Name, Title, Contact Number, Email, Website, Social Media, Address
Requirements
Must have
- Clean & Simple but Serious and Impressionable

```html
<!DOCTYPE html>
<html lang="en">
<head>
<meta charset="utf-8">
<title>Corvane Hospitality Reps – Business Card</title>
<link rel="stylesheet" href="https://fonts.googleapis.com/css2?family=Montserrat:wght@400;500;700&display=swap">
<style>
  :root {
    --navy: #2e2f78;
    --ink: #1d1d24;
    --paper: #ffffff;
    --backdrop: #e5e5e6;
  }
  * { margin: 0; padding: 0; box-sizing: border-box; }
  html, body {
    width: 1200px; height: 1200px; overflow: hidden;
    background: var(--backdrop);
    font-family: "Montserrat", Arial, sans-serif;
  }
  .card {
    position: absolute; left: 136px; width: 928px; height: 543px;
    background: var(--paper);
    box-shadow: 0 3px 10px rgba(0,0,0,0.18);
  }
  .card-front { top: 41px; }
  .card-back { top: 610px; }

  .brand-name-front {
    position: absolute; left: 82px; top: 160px;
    color: var(--navy); font-weight: 700; font-size: 84px; letter-spacing: -1px;
    display: flex; align-items: center; gap: 22px;
  }
  .brand-dot {
    width: 34px; height: 34px; border-radius: 50%; background: var(--navy);
  }

  .holder {
    position: absolute; right: 64px; top: 136px; text-align: right; color: var(--navy);
  }
  .holder-name { font-weight: 700; font-size: 37px; line-height: 1.1; }
  .holder-title { font-weight: 500; font-size: 21px; margin-top: 2px; }

  .contact-list {
    position: absolute; right: 60px; top: 236px; list-style: none;
  }
  .contact-item {
    display: flex; justify-content: flex-end; align-items: center;
    gap: 18px; height: 39px; font-size: 22px; color: var(--ink);
  }
  .contact-item svg { width: 16px; height: 16px; fill: var(--navy); }

  .address-band {
    position: absolute; left: 0; right: 0; top: 423px; height: 74px;
    background: var(--navy); color: var(--paper);
    display: flex; justify-content: flex-end; align-items: center;
    gap: 22px; padding-right: 64px; font-size: 21px;
  }
  .address-band svg { width: 14px; height: 16px; fill: var(--paper); }

  .brand-lockup {
    position: absolute; left: 0; right: 0; top: 205px;
    display: flex; justify-content: center; align-items: center; gap: 20px;
    color: var(--navy); font-weight: 700; font-size: 46px; letter-spacing: 1px;
  }
  .brand-lockup .brand-dot { width: 26px; height: 26px; }
</style>
</head>
<body>

<section class="card card-front">
  <div class="brand-name-front"><span class="brand-dot"></span>Corvane</div>

  <div class="holder">
    <div class="holder-name">Marin Okafor</div>
    <div class="holder-title">Director</div>
  </div>

  <ul class="contact-list">
    <li class="contact-item">(555) 240-7316
      <svg viewBox="0 0 16 16" aria-hidden="true"><path d="M3.5 1l2.5 3-1.5 1.5c.8 2 2.2 3.4 4.2 4.3L10.2 8.3l3.3 2.4-1 3c-.3.8-1.2 1.2-2 .9C5.9 13.2 2.6 9.8 1.3 5.2 1 4.4 1.4 3.5 2.2 3.2z"/></svg>
    </li>
    <li class="contact-item">(555) 240-7390
      <svg viewBox="0 0 16 16" aria-hidden="true"><path d="M4 1h8v4H4zM1 6h14v6h-3v3H4v-3H1zM5 10v4h6v-4z"/></svg>
    </li>
    <li class="contact-item">www.corvanereps.com
      <svg viewBox="0 0 16 16" aria-hidden="true"><path d="M8 1a7 7 0 100 14A7 7 0 008 1zm0 1.3c.9 1 1.5 2.4 1.7 4.1H6.3C6.5 4.7 7.1 3.3 8 2.3zM2.4 7.4h2.9c0 .5 0 1 .1 1.3H2.4a5.7 5.7 0 010-1.3zm4 0h3.3a8 8 0 010 1.3H6.3a8 8 0 010-1.3zm4.3 0h2.9a5.7 5.7 0 010 1.3h-2.9c0-.4.1-.9 0-1.3zM6.3 9.7h3.4c-.2 1.7-.8 3-1.7 4-.9-1-1.5-2.3-1.7-4z"/></svg>
    </li>
  </ul>

  <div class="address-band">DNP, APRN 4100 Linden Crest Way Fairhaven, FL 30215
    <svg viewBox="0 0 14 16" aria-hidden="true"><path d="M7 0a5.5 5.5 0 00-5.5 5.5C1.5 9.5 7 16 7 16s5.5-6.5 5.5-10.5A5.5 5.5 0 007 0zm0 7.7a2.2 2.2 0 110-4.4 2.2 2.2 0 010 4.4z"/></svg>
  </div>
</section>

<section class="card card-back">
  <div class="brand-lockup"><span class="brand-dot"></span>CORVANE HOSPITALITY REPS</div>
</section>

</body>
</html>
```